Kestrelmoor Advisory Services LLC
The Quiet Hand Consutants
Project: Kestrelmoor Advisory Services LLC
Kestrelmoor Advisory Services LLC - Financial Services
Creative Brief
Professional
Warrick Dunstan Hollowell
Senior Managing Director
388 West 19th Street New York, N.T. 10024
whollowell@kmaservices.net
KESTRELMOORADVISORYSERVICES.COM

```html
<!DOCTYPE html>
<html lang="en">
<head>
<meta charset="utf-8">
<title>Kestrelmoor Advisory Services – Business Card</title>
<link rel="stylesheet" href="https://fonts.googleapis.com/css2?family=Cinzel:wght@400;600&family=Questrial&display=swap">
<style>
  :root {
    --backdrop: #6e4b2c;
    --card: #ffffff;
    --ink: #2b2b2b;
    --brand-blue: #1a5fa8;
    --band-blue: #1c6dc0;
    --band-deep: #0f4f96;
    --gold: #d4a63a;
    --white: #ffffff;
  }
  * { box-sizing: border-box; margin: 0; padding: 0; }
  html, body { width: 1200px; height: 406px; overflow: hidden; }
  body { background: var(--backdrop); position: relative; font-family: "Questrial", sans-serif; }

  .card {
    position: absolute; top: 46px; width: 516px; height: 318px;
    background: var(--card); border-radius: 14px; overflow: hidden;
    box-shadow: 0 2px 6px rgba(0,0,0,.35);
  }
  .card--front { left: 68px; }
  .card--back { left: 616px; }

  .swoosh { position: absolute; left: 0; bottom: 0; width: 100%; height: 140px; }

  .website {
    position: absolute; left: 22px; bottom: 12px;
    color: var(--white); font-size: 12.5px; letter-spacing: .2px;
  }

  .brand { position: absolute; color: var(--brand-blue); font-family: "Cinzel", serif; font-weight: 600; text-transform: uppercase; line-height: 1.15; }
  .brand__mark { display: block; border-radius: 50%; background: var(--brand-blue); }

  .card--front .brand { left: 26px; top: 44px; width: 240px; text-align: center; font-size: 22px; }
  .card--front .brand__mark { width: 70px; height: 70px; margin: 0 auto 12px; }

  .card--back .brand { left: 0; right: 0; top: 34px; text-align: center; font-size: 27px; }
  .card--back .brand__mark { width: 96px; height: 96px; margin: 0 auto 14px; }

  .person { position: absolute; right: 22px; top: 14px; text-align: right; color: var(--ink); }
  .person__name { font-family: "Cinzel", serif; font-weight: 600; font-size: 15px; letter-spacing: .5px; }
  .person__title { font-family: "Cinzel", serif; font-size: 11px; margin-top: 5px; }

  .contact { position: absolute; right: 26px; top: 118px; width: 200px; color: var(--ink); font-size: 13px; line-height: 1.45; }
  .contact__address { margin-bottom: 18px; padding-left: 34px; }
  .contact__lines { list-style: none; }
</style>
</head>
<body>

<section class="card card--front" aria-label="Business card front">
  <svg class="swoosh" viewBox="0 0 516 140" preserveAspectRatio="none" aria-hidden="true">
    <path d="M0 70 C150 120 330 110 516 40 L516 58 C330 125 150 132 0 88 Z" fill="var(--gold)"/>
    <path d="M0 92 C160 138 340 126 516 60 L516 140 L0 140 Z" fill="var(--band-blue)"/>
    <path d="M0 118 C180 142 360 128 516 84 L516 140 L0 140 Z" fill="var(--band-deep)" opacity=".55"/>
  </svg>

  <div class="brand">
    <span class="brand__mark"></span>
    Kestrelmoor Advisory Services
  </div>

  <div class="person">
    <p class="person__name">Warrick Dunstan Hollowell</p>
    <p class="person__title">Senior Managing Director</p>
  </div>

  <div class="contact">
    <p class="contact__address">614 Larkspur Avenue<br>Fairmont, WV 26554</p>
    <ul class="contact__lines">
      <li>P : 646-555-0142</li>
      <li>C : 201-555-0187</li>
      <li>F : 917-555-0119</li>
      <li>E : whollowell@kmaservices.net</li>
    </ul>
  </div>

  <p class="website">www.kestrelmooradvisoryservices.com</p>
</section>

<section class="card card--back" aria-label="Business card back">
  <svg class="swoosh" viewBox="0 0 516 140" preserveAspectRatio="none" aria-hidden="true">
    <path d="M0 70 C150 120 330 110 516 40 L516 58 C330 125 150 132 0 88 Z" fill="var(--gold)"/>
    <path d="M0 92 C160 138 340 126 516 60 L516 140 L0 140 Z" fill="var(--band-blue)"/>
    <path d="M0 118 C180 142 360 128 516 84 L516 140 L0 140 Z" fill="var(--band-deep)" opacity=".55"/>
  </svg>

  <div class="brand">
    <span class="brand__mark"></span>
    Kestrelmoor Advisory<br>Services
  </div>

  <p class="website">www.kestrelmooradvisoryservices.com</p>
</section>

</body>
</html>
```